'We're just a little bit different' business cards for an IT Startup

We are an Information Technology Start-up focusing on providing IT strategy services to large midcap and enterprise organisations. We need to create business cards which reflect us personally and our brand. Clarvane.io is looking to differentiate itself in the market by providing IT strategy that reflects Information technology today.
We would like business cards that:
- Are just a little bit different, so people read them
- Reflect that Clarvane.Io is a modern disruptive technology company
- Reinforces our brand – strategy reinvented
- Provides information about us that is deeper and richer than just here’s my mobile and email address. We’d like the business card to be a snapshot of who we individually. It might be fav movie, book, sports, favourite beer, my family etc, fav quote etc

I have attached a document which has details about me to use on a sample business card and it also includes snapshots of our website. Also attached is our logo. If you need more information please ask

Industry/Entity Type

Information Technology

Contact Information for Business Card

See attached document, for my personal details to use as a sample

Requirements
Must have
• my details
• web site - url clarvane.io
• something a little bit different
Nice to have
• I'd like to see the design incorporate information about us that lets them see us as fellow human beings not just a work person
Should not have
• standard bland business cards

```html
<!DOCTYPE html>
<html lang="en">
<head>
<meta charset="utf-8">
<title>Clarvane.io — Business Card</title>
<link rel="stylesheet" href="https://fonts.googleapis.com/css2?family=Open+Sans:wght@400;600;700&display=swap">
<style>
  :root {
    --bg: #2a2a2c;
    --card: #f7f7f7;
    --ink: #3a3a3e;
    --red: #e8473b;
    --blue: #1a78ae;
    --orange: #f3961f;
    --pink: #cc4f78;
    --plum: #8f3f68;
    --white: #ffffff;
    --font: "Open Sans", Arial, sans-serif;
  }
  * { box-sizing: border-box; margin: 0; padding: 0; }
  html, body { width: 1200px; height: 900px; overflow: hidden; }
  body { background: var(--bg); font-family: var(--font); position: relative; }

  .card {
    position: absolute;
    left: 260px;
    width: 680px;
    height: 388px;
    background: var(--card);
    border-radius: 14px;
  }
  .card--front { top: 44px; }
  .card--back { top: 468px; }

  .stripe { position: absolute; display: flex; gap: 3px; height: 4px; }
  .stripe span { flex: 1; }
  .c-red { background: var(--red); }
  .c-blue { background: var(--blue); }
  .c-orange { background: var(--orange); }
  .c-pink { background: var(--pink); }
  .c-plum { background: var(--plum); }

  .brand-name {
    position: absolute;
    font-weight: 600;
    color: var(--ink);
    line-height: 1;
    white-space: nowrap;
  }

  /* front */
  .card--front .stripe--top { left: 48px; right: 40px; top: 42px; }
  .card--front .stripe--low { left: 300px; right: 40px; top: 300px; }
  .card--front .brand-name { left: 0; right: 0; text-align: center; top: 160px; font-size: 64px; }

  /* back */
  .tiles { position: absolute; left: 44px; top: 26px; display: flex; gap: 4px; }
  .tile { width: 118px; display: flex; flex-direction: column; gap: 4px; }
  .tile__rule { height: 3px; }
  .tile__box {
    height: 86px;
    display: flex;
    flex-direction: column;
    align-items: center;
    justify-content: center;
    gap: 8px;
    color: var(--white);
    font-size: 11.5px;
    line-height: 1.25;
    text-align: center;
    padding: 0 6px;
  }
  .tile__box svg { width: 24px; height: 24px; }
  .family-icon { width: 30px; height: 24px; background: rgba(255,255,255,0.85); border-radius: 3px; }

  .card--back .brand-name { left: 46px; top: 238px; font-size: 54px; }

  .person { position: absolute; left: 390px; top: 150px; width: 260px; text-align: center; }
  .person__avatar { width: 32px; height: 32px; border-radius: 50%; background: var(--blue); margin: 0 auto 6px; }
  .person__name { font-size: 30px; font-weight: 700; color: var(--blue); line-height: 1.1; white-space: nowrap; }
  .person__role { font-size: 18px; color: var(--red); margin-top: 2px; }

  .card--back .stripe--bottom { left: 44px; right: 44px; top: 346px; }
</style>
</head>
<body>

<section class="card card--front">
  <div class="stripe stripe--top">
    <span class="c-red"></span><span class="c-blue"></span><span class="c-orange"></span><span class="c-pink"></span><span class="c-plum"></span>
  </div>
  <div class="brand-name">Clarvane</div>
  <div class="stripe stripe--low">
    <span class="c-blue"></span><span class="c-orange"></span><span class="c-pink"></span><span class="c-plum"></span>
  </div>
</section>

<section class="card card--back">
  <div class="tiles">
    <div class="tile">
      <div class="tile__rule c-red"></div>
      <div class="tile__box c-red">
        <svg viewBox="0 0 24 24" fill="none" stroke="#fff" stroke-width="1.6"><circle cx="12" cy="12" r="10.5"/><path d="M8.5 7.5l1.8-.5 1.2 2.6-1.3 1c.6 1.4 1.6 2.4 3 3l1-1.3 2.6 1.2-.5 1.8c-4 .4-8.2-3.8-7.8-7.8z" fill="#fff" stroke="none"/></svg>
        <span>0400738264</span>
      </div>
    </div>
    <div class="tile">
      <div class="tile__rule c-blue"></div>
      <div class="tile__box c-blue">
        <svg viewBox="0 0 24 24" fill="none" stroke="#fff" stroke-width="1.4"><rect x="2" y="5" width="20" height="14"/><polyline points="2,5 12,13 22,5"/><line x1="2" y1="19" x2="9.5" y2="11"/><line x1="22" y1="19" x2="14.5" y2="11"/></svg>
        <span>owen@clarvane.io</span>
      </div>
    </div>
    <div class="tile">
      <div class="tile__rule c-orange"></div>
      <div class="tile__box c-orange">
        <svg viewBox="0 0 24 24" fill="none" stroke="#fff" stroke-width="1.4"><circle cx="12" cy="12" r="10"/><ellipse cx="12" cy="12" rx="4.5" ry="10"/><line x1="2" y1="12" x2="22" y2="12"/><line x1="4" y1="7" x2="20" y2="7"/><line x1="4" y1="17" x2="20" y2="17"/></svg>
        <span>www.clarvane.io</span>
      </div>
    </div>
    <div class="tile">
      <div class="tile__rule c-pink"></div>
      <div class="tile__box c-pink">
        <svg viewBox="0 0 24 24" fill="none" stroke="#fff" stroke-width="1.6"><path d="M12 22s-7-7.5-7-12.5a7 7 0 0 1 14 0C19 14.5 12 22 12 22z"/><circle cx="12" cy="9.5" r="2.5"/></svg>
        <span>Your Address<br>In Two Line</span>
      </div>
    </div>
    <div class="tile">
      <div class="tile__rule c-plum"></div>
      <div class="tile__box c-plum">
        <div class="family-icon" role="img" aria-label="Small family icon: house with parents and children"></div>
        <span>Elena my wife<br>and 4 children</span>
      </div>
    </div>
  </div>

  <div class="brand-name">Clarvane</div>

  <div class="person">
    <div class="person__avatar" role="img" aria-label="Profile avatar icon"></div>
    <div class="person__name">Owen Hartley</div>
    <div class="person__role">Founder</div>
  </div>

  <div class="stripe stripe--bottom">
    <span class="c-red"></span><span class="c-blue"></span><span class="c-orange"></span><span class="c-pink"></span><span class="c-plum"></span>
  </div>
</section>

</body>
</html>
```